I require a set of preaching screens for our Easter weekend.

1. Good Friday Service Title: The Lantern
2. Easter Sunday Service Title Bright Harbor
3. Message Title Screen Title Bright Harbor
Overview
We need a set of clean, minimal screen graphics for 3 service sermon series called Bright Harbor
All screens must be delivered at 1920x1080px (16:9), suitable for projection in a church auditorium.

Design style
Minimal and clean. Uncluttered. Strong typography. Subtle use of imagery or texture — nothing busy or overly decorative.

The tone should feel thoughtful and weighty without being dark or heavy.

Subtitle: Letters Along the Road to the River
Date range: 1 March – 5 April

Branding
No existing branding to match. Designer has creative freedom on colour palette and typography, provided the overall feel remains minimal and clean.
What to avoid
Busy backgrounds or heavy textures
All files in PNG at 1920x1080px
Editable source files (PSD or AI)

Please use images below as you feel is appropriate - we have permission for these - We want to see a at least three options for these screens to .

We need designs within 3 days

```html
<!DOCTYPE html>
<html lang="en">
<head>
<meta charset="utf-8">
<title>Bright Harbor – Easter Screen Set</title>
<link rel="stylesheet" href="https://fonts.googleapis.com/css2?family=Playfair+Display:wght@500;600&family=Libre+Baskerville:wght@400;700&display=swap">
<style>
  :root {
    --stage-left: #eef3f2;
    --stage-mid: #d3e2e0;
    --stage-right: #b9d1d2;
    --peach: #f8b4a0;
    --apricot: #fdd3a8;
    --cream: #f3efe6;
    --butter: #eef0d2;
    --mist: #f1f0f8;
    --lavender: #d2d0f3;
    --periwinkle: #c6d6f4;
    --blush: #f5e6f6;
    --rose: #fcdcd8;
    --lilac: #cbb8e0;
    --orchid: #c56fb4;
    --plum: #a45aa0;
    --ink: #4d4750;
    --sky-ink: #4a89c9;
    --white: #ffffff;
  }
  * { box-sizing: border-box; margin: 0; padding: 0; }
  html, body { width: 1200px; height: 1200px; overflow: hidden; }
  body {
    background: linear-gradient(90deg, var(--stage-left) 0%, var(--stage-mid) 55%, var(--stage-right) 100%);
    position: relative;
    font-family: "Libre Baskerville", Georgia, serif;
  }
  .screen {
    position: absolute;
    left: 306px;
    width: 654px;
    height: 368px;
    overflow: hidden;
    display: flex;
    flex-direction: column;
    align-items: center;
    justify-content: center;
    box-shadow: 0 1px 3px rgba(60, 80, 80, 0.08);
  }
  .screen--friday {
    top: 17px;
    background:
      radial-gradient(ellipse 40% 45% at 0% 0%, var(--butter) 0%, transparent 80%),
      radial-gradient(ellipse 30% 60% at 100% 20%, var(--apricot) 0%, transparent 75%),
      radial-gradient(ellipse 70% 40% at 50% 100%, var(--peach) 0%, transparent 85%),
      radial-gradient(ellipse 60% 50% at 60% 30%, var(--mist) 0%, transparent 80%),
      var(--cream);
  }
  .screen--sunday {
    top: 410px;
    background:
      radial-gradient(ellipse 35% 60% at 0% 60%, var(--blush) 0%, transparent 80%),
      radial-gradient(ellipse 30% 50% at 100% 85%, var(--white) 0%, transparent 70%),
      radial-gradient(ellipse 55% 55% at 70% 45%, var(--periwinkle) 0%, transparent 85%),
      linear-gradient(160deg, #ecebf8 0%, var(--lavender) 50%, #cacdf3 100%);
  }
  .screen--message {
    top: 814px;
    background:
      radial-gradient(ellipse 35% 45% at 0% 10%, var(--lilac) 0%, transparent 80%),
      radial-gradient(ellipse 30% 40% at 95% 20%, #d8cff5 0%, transparent 80%),
      radial-gradient(ellipse 30% 35% at 0% 95%, #d7c8e6 0%, transparent 80%),
      radial-gradient(ellipse 60% 55% at 55% 55%, var(--rose) 0%, transparent 90%),
      #f3d9e1;
  }
  .church-mark {
    display: flex;
    align-items: center;
    gap: 6px;
    margin-bottom: 8px;
    font-family: "Libre Baskerville", Georgia, serif;
    font-size: 11px;
    font-weight: 400;
    letter-spacing: 0.08em;
    color: var(--white);
  }
  .church-mark__dot {
    width: 14px; height: 14px;
    border-radius: 50%;
    background: var(--white);
    opacity: 0.9;
  }
  .series-title {
    font-family: "Playfair Display", "Times New Roman", serif;
    font-weight: 600;
    font-size: 62px;
    line-height: 1;
    letter-spacing: -0.01em;
    transform: scaleX(0.86);
    white-space: nowrap;
  }
  .screen--friday .series-title {
    background: linear-gradient(180deg, #d98fc6 0%, var(--orchid) 55%, var(--plum) 100%);
    -webkit-background-clip: text; background-clip: text; color: transparent;
  }
  .screen--sunday .series-title {
    background: linear-gradient(180deg, #fdf3ea 0%, #f4cdb7 55%, #e9b9a3 100%);
    -webkit-background-clip: text; background-clip: text; color: transparent;
    filter: drop-shadow(0 0 2px rgba(255,255,255,0.8));
  }
  .screen--message .series-title {
    text-transform: uppercase;
    font-size: 58px;
    background: linear-gradient(180deg, #ffffff 0%, #d7ecf7 45%, #a9d3ec 100%);
    -webkit-background-clip: text; background-clip: text; color: transparent;
    filter: drop-shadow(0 0 1.5px #ffffff) drop-shadow(0 2px 3px rgba(170,140,170,0.35));
  }
  .series-subtitle {
    margin-top: 6px;
    font-size: 9px;
    font-weight: 700;
    letter-spacing: 0.01em;
  }
  .screen--friday .series-subtitle { color: var(--ink); }
  .screen--sunday .series-subtitle { color: var(--white); margin-top: 2px; }
  .screen--message .series-subtitle { color: var(--sky-ink); }
</style>
</head>
<body>
  <section class="screen screen--friday" aria-label="Good Friday service title screen">
    <div class="church-mark"><span class="church-mark__dot"></span>Harborlight</div>
    <h1 class="series-title">The Lantern</h1>
    <p class="series-subtitle">Letters Along the Road to the River</p>
  </section>

  <section class="screen screen--sunday" aria-label="Easter Sunday service title screen">
    <div class="church-mark"><span class="church-mark__dot"></span>Harborlight</div>
    <h1 class="series-title">Bright Harbor</h1>
    <p class="series-subtitle">Letters Along the Road to the River</p>
  </section>

  <section class="screen screen--message" aria-label="Message title screen">
    <div class="church-mark"><span class="church-mark__dot"></span>Harborlight</div>
    <h1 class="series-title">Bright Harbor</h1>
    <p class="series-subtitle">Letters Along the Road to the River</p>
  </section>
</body>
</html>
```